Pelican Litigation Funding Letterhead & Document Template

We need a letter head designed for our fund. Our fund works with law firms and investors across the globe. We need a a cover letter template as well as a document template for subsequent pages. Blue and white color scheme is preferred. This is our predecessor's website: https://www.pelicanvq.com/index.html. Please see our logo attached. The logo color code is #19478d. Font is Gotham-Medium.
Target Market(s)
Sophisticated investors and law firms
Font styles to use
Sans Serif
Colors
0255a3

```html
<!DOCTYPE html>
<html lang="en">
<head>
<meta charset="utf-8">
<title>Pelican Litigation Funding Letterhead</title>
<link href="https://fonts.googleapis.com/css2?family=Montserrat:wght@300;400;500&display=swap" rel="stylesheet">
<style>
  :root {
    --brand-blue: #19478d;
    --paper: #ffffff;
    --backdrop: #ececec;
    --footer-text: #ffffff;
    --rule-light: rgba(255,255,255,0.45);
  }
  * { box-sizing: border-box; margin: 0; padding: 0; }
  html, body {
    width: 1200px; height: 1200px; overflow: hidden;
    background: var(--backdrop);
    font-family: "Montserrat", sans-serif;
  }
  .letterhead {
    position: absolute;
    left: 160px; top: 30px;
    width: 880px; height: 1140px;
    background: var(--paper);
    box-shadow: 0 2px 10px rgba(0,0,0,0.12);
    overflow: hidden;
  }
  .letterhead__brand {
    position: absolute;
    top: 156px; left: 0; width: 100%;
    text-align: center;
    color: var(--brand-blue);
    font-weight: 500;
    font-size: 26px;
    letter-spacing: 1.5px;
    text-transform: uppercase;
  }
  .letterhead__footer-art {
    position: absolute;
    left: 0; bottom: 0;
    width: 880px; height: 140px;
    display: block;
  }
  .letterhead__contact {
    position: absolute;
    left: 81px; width: 719px;
    bottom: 22px;
    color: var(--footer-text);
    font-weight: 300;
    font-size: 15px;
    letter-spacing: 0.4px;
  }
  .contact__address {
    padding-bottom: 6px;
    border-bottom: 1px solid var(--rule-light);
    white-space: nowrap;
    text-align: center;
  }
  .contact__lines {
    display: flex;
    justify-content: space-between;
    padding-top: 7px;
    white-space: nowrap;
  }
  .contact__item { display: inline-flex; align-items: center; gap: 6px; }
  .contact__icon { width: 11px; height: 11px; fill: var(--footer-text); }
</style>
</head>
<body>
  <main class="letterhead">
    <div class="letterhead__brand">Pelican Litigation Funding</div>

    <svg class="letterhead__footer-art" viewBox="0 1220 1074 171" preserveAspectRatio="none" aria-hidden="true">
      <polygon fill="#19478d" points="0,1291 538,1230 1074,1289 538,1246"/>
      <polygon fill="#19478d" points="0,1296 538,1252 1074,1294 1074,1391 0,1391"/>
    </svg>

    <div class="letterhead__contact">
      <p class="contact__address">Bayview Tower - Executive Level, 4180 Lantern Avenue, Suite 2210, Dallas, Texas, 75000</p>
      <div class="contact__lines">
        <span class="contact__item">
          <svg class="contact__icon" viewBox="0 0 24 24"><path d="M6.6 10.8a15.1 15.1 0 0 0 6.6 6.6l2.2-2.2a1 1 0 0 1 1-.25 11.4 11.4 0 0 0 3.6.57 1 1 0 0 1 1 1V20a1 1 0 0 1-1 1A17 17 0 0 1 3 4a1 1 0 0 1 1-1h3.5a1 1 0 0 1 1 1c0 1.25.2 2.45.57 3.6a1 1 0 0 1-.25 1z"/></svg>
          (555) 014-2481
        </span>
        <span class="contact__item">
          <svg class="contact__icon" viewBox="0 0 24 24"><path d="M6 2h12v6H6z M3 9h18v9h-3v4H6v-4H3z M8 15v5h8v-5z"/></svg>
          (555) 014-2482
        </span>
        <span class="contact__item">
          <svg class="contact__icon" viewBox="0 0 24 24"><path d="M2 5h20v14H2z M4 7v1l8 5 8-5V7l-8 5z" fill-rule="evenodd"/></svg>
          info@pelicanvq.com
        </span>
        <span class="contact__item">
          <svg class="contact__icon" viewBox="0 0 24 24"><path d="M12 2a10 10 0 1 0 0 20 10 10 0 0 0 0-20zm0 2c.9 1.2 1.6 2.9 1.9 5h-3.8c.3-2.1 1-3.8 1.9-5zm-2.4.4A12 12 0 0 0 8.1 9H4.9a8 8 0 0 1 4.7-4.6zm4.8 0A8 8 0 0 1 19.1 9h-3.2a12 12 0 0 0-1.5-4.6zM4.3 11h3.6v2H4.3a8 8 0 0 1 0-2zm5.6 0h4.2v2H9.9zm6.2 0h3.6a8 8 0 0 1 0 2h-3.6zM4.9 15h3.2a12 12 0 0 0 1.5 4.6A8 8 0 0 1 4.9 15zm5.2 0h3.8c-.3 2.1-1 3.8-1.9 5-.9-1.2-1.6-2.9-1.9-5zm5.8 0h3.2a8 8 0 0 1-4.7 4.6 12 12 0 0 0 1.5-4.6z"/></svg>
          www.pelicanvq.com
        </span>
      </div>
    </div>
  </main>
</body>
</html>
```